Brookvale Renovations - Get the creative juices going!!

Brookvale does not do the actual renovation work. The company provides high end project management of renovation (primarily residential - with an eye toward commercial) The renovation work could look very different between projects. This company manages the work of contractors, architects and interior designers (either subcontracted directly by Brookvale or hired by the client and entrusted to Brookvale to manage). Clients are high end in the economic scale and the card needs to have a high end feel to it.

The owner is female, but the audience will be heavily slanted male. It should not be a "feminine" or "masculine" looking card. If anything, slant more on the masculine side. Clean, simple, yet creative and artistically appealing. The card design should complement and in no way compete with the logo.

When people think of our company: trust, integrity, dynamic, limitless possibilities, transition, energy, creative. We plan to expand in the future to be international.

There will also be a contest running for stationary. Please check that section, as well.

***Black is 80-90 percent black. Not stark black

Tight timeline. Needs cards printed quickly!

```html
<!DOCTYPE html>
<html lang="en">
<head>
<meta charset="utf-8">
<title>Brookvale Renovations – Business Card</title>
<link rel="stylesheet" href="https://fonts.googleapis.com/css2?family=Lato:wght@400;700&display=swap">
<style>
  :root {
    --page-bg: #2a2a2a;
    --card-bg: #2b2c2d;
    --teal: #17a99c;
    --white: #f4f4f4;
    --soft-text: #e6e6e6;
  }
  html, body {
    margin: 0;
    padding: 0;
    width: 1200px;
    height: 1000px;
    overflow: hidden;
    background: var(--page-bg);
  }
  .canvas {
    width: 1200px;
    height: 1000px;
    display: flex;
    align-items: center;
    justify-content: center;
  }
  .business-card {
    position: relative;
    width: 1000px;
    height: 572px;
    background: var(--card-bg);
    border-radius: 14px;
    overflow: hidden;
    font-family: "Lato", sans-serif;
    color: var(--soft-text);
  }
  .brand {
    position: absolute;
    left: 80px;
    top: 110px;
    display: flex;
    align-items: center;
    gap: 22px;
  }
  .brand-square {
    width: 64px;
    height: 64px;
    background: var(--teal);
  }
  .brand-name {
    font-size: 44px;
    font-weight: 700;
    letter-spacing: 3px;
    color: var(--white);
    text-transform: uppercase;
  }
  .person {
    position: absolute;
    left: 110px;
    top: 232px;
  }
  .person-name {
    margin: 0;
    font-size: 40px;
    font-weight: 700;
    color: var(--teal);
    letter-spacing: 1px;
    text-transform: uppercase;
  }
  .person-title {
    margin: 4px 0 0;
    font-size: 24px;
  }
  .contact-list {
    position: absolute;
    left: 140px;
    top: 330px;
    margin: 0;
    padding: 0;
    list-style: none;
    font-size: 25px;
    line-height: 34px;
  }
  .contact-label {
    color: var(--teal);
    font-weight: 700;
    margin-right: 6px;
  }
  .address {
    position: absolute;
    left: 140px;
    top: 478px;
    margin: 0;
    font-size: 25px;
  }
  .edge-stripe {
    position: absolute;
    left: 0;
    right: 0;
    bottom: 0;
    height: 26px;
    background: var(--teal);
    border-top: 8px solid var(--white);
  }
</style>
</head>
<body>
<main class="canvas">
  <article class="business-card">
    <header class="brand">
      <span class="brand-square" aria-hidden="true"></span>
      <span class="brand-name">Brookvale Reno</span>
    </header>

    <section class="person">
      <h1 class="person-name">Your Name</h1>
      <p class="person-title">Title</p>
    </section>

    <ul class="contact-list">
      <li><span class="contact-label">P:</span>555 014 2368</li>
      <li><span class="contact-label">F:</span>555 019 7742</li>
      <li><span class="contact-label">E:</span>yourname@brookvalereno.com</li>
      <li><span class="contact-label">W:</span>www.brookvalereno.com</li>
    </ul>

    <p class="address">Street 04, Suite 210, Elm Road, Fairview, US 5678</p>

    <div class="edge-stripe" aria-hidden="true"></div>
  </article>
</main>
</body>
</html>
```